Product Design Images for website use and social media

I need product images edited to be posted on website and our socialmedia pages
All need to be of similar design style
minimalist, modern and bright highlighting natural wood elements
products are
-coffee table with matching coasters
- piano key coat racks large and small
- cheese board
- clock

some designs i like can be seen at https://www.brackenloftjoinery.com/for-sale

Target Market(s)

general public, home wares and home designs

Industry/Entity Type

homewares interior designs

Requirements
Should not have
• clutter or be too busy

```html
<!DOCTYPE html>
<html lang="en">
<head>
<meta charset="utf-8">
<title>Product Design Images – Another Style</title>
<link rel="stylesheet" href="https://fonts.googleapis.com/css2?family=Arimo:wght@700&family=Open+Sans:ital,wght@0,300;0,400;1,300;1,400;1,800&display=swap">
<style>
  :root {
    --sand: #b89d80;
    --ink: #1a1a1a;
    --white: #ffffff;
    --walnut: #733a31;
    --charcoal: #352e2f;
    --rule: #5a3f36;
    --dot-dark: #3b2a22;
    --dot-mid: #6b3a32;
    --offer-red: #ff3333;
    --copy: #2b2b2b;
  }
  * { margin: 0; padding: 0; box-sizing: border-box; }
  html, body { width: 1200px; height: 1200px; overflow: hidden; }
  body {
    background: var(--sand);
    position: relative;
    font-family: "Open Sans", Arial, sans-serif;
  }
  .board-title {
    position: absolute; top: 122px; left: 0; width: 1200px;
    text-align: center;
    font-weight: 800; font-style: italic;
    font-size: 47px; letter-spacing: 7px;
    color: var(--ink);
  }
  .board-subtitle {
    position: absolute; top: 205px; left: 0; width: 1200px;
    text-align: center;
    font-weight: 400; font-style: italic;
    font-size: 30px; letter-spacing: 5px;
    color: var(--white);
  }
  .board-note {
    position: absolute; top: 971px; left: 0; width: 1200px;
    text-align: center;
    font-weight: 300; font-style: italic;
    font-size: 22px; letter-spacing: 4px;
    color: var(--white);
  }
  .product-card {
    position: absolute; top: 365px;
    width: 469px; height: 470px;
    background: var(--white);
  }
  .product-card--clock { left: 120px; }
  .product-card--rack { left: 612px; }
  .card-frame { position: absolute; left: 0; top: 0; }
  .product-photo { position: absolute; }
  .product-photo--clock {
    left: 31px; top: 145px; width: 250px; height: 280px;
    border-radius: 46% 52% 48% 50%;
    background: radial-gradient(circle at 50% 50%, #8a3a45 0%, #7a3038 55%, #b0622e 100%);
  }
  .product-photo--rack {
    left: 40px; top: 290px; width: 290px; height: 52px;
    transform: rotate(-33deg);
    border-radius: 4px;
    background: linear-gradient(90deg, #151515 0%, #2a1515 50%, #8a2f2a 100%);
  }
  .label { position: absolute; color: var(--white); font-style: italic; font-weight: 800; display: flex; align-items: center; justify-content: center; }
  .label--wall { left: 344px; top: 134px; width: 98px; height: 54px; background: var(--walnut); font-size: 24px; letter-spacing: 2px; padding-left: 6px; }
  .label--clock { left: 392px; top: 204px; width: 50px; height: 23px; background: var(--charcoal); font-size: 10px; letter-spacing: 1.5px; }
  .label--piano { left: 283px; top: 105px; width: 157px; height: 55px; background: var(--ink); font-size: 24px; letter-spacing: 2.5px; }
  .label--size { left: 315px; top: 168px; width: 125px; height: 24px; background: var(--walnut); font-size: 10px; letter-spacing: 1.3px; }
  .product-copy {
    position: absolute; text-align: right;
    font-weight: 300; font-size: 13px; line-height: 18px;
    color: var(--copy);
  }
  .product-copy--clock { right: 27px; top: 280px; width: 160px; }
  .product-copy--rack { right: 28px; top: 277px; width: 160px; }
  .end-rule { position: absolute; height: 1px; background: var(--walnut); top: 424px; }
  .end-rule--clock { left: 297px; width: 145px; }
  .end-rule--rack { left: 296px; width: 145px; }
  .offer-ribbon text { font-family: Arimo, Arial, sans-serif; font-weight: 700; fill: var(--white); }
</style>
</head>
<body>
  <h1 class="board-title">PRODUCT DESIGN IMAGES</h1>
  <p class="board-subtitle">ANOTHER STYLE</p>

  <article class="product-card product-card--clock">
    <div class="product-photo product-photo--clock" role="img" aria-label="Photo of a natural burl wood wall clock with black numerals and hands"></div>
    <svg class="card-frame offer-ribbon" width="469" height="300" viewBox="0 0 469 300">
      <circle cx="34" cy="42" r="5" fill="var(--dot-dark)"/>
      <circle cx="48" cy="42" r="5" fill="var(--dot-mid)"/>
      <circle cx="61" cy="42" r="5" fill="var(--offer-red)"/>
      <polyline points="442,60 29,60 29,261" fill="none" stroke="var(--rule)" stroke-width="1.2"/>
      <polygon points="91,61 148,61 29,180 29,123" fill="var(--offer-red)"/>
      <text x="65" y="98" font-size="9" text-anchor="middle" transform="rotate(-45 65 98)">SPECIAL</text>
      <text x="82" y="112" font-size="24" text-anchor="middle" transform="rotate(-45 82 112)">OFFER</text>
    </svg>
    <div class="label label--wall">WALL</div>
    <div class="label label--clock">CLOCK</div>
    <p class="product-copy product-copy--clock">A modern wall clock crafted in natural wood tones. Simple yet striking, combining functionality with timeless design.</p>
    <div class="end-rule end-rule--clock"></div>
  </article>

  <article class="product-card product-card--rack">
    <div class="product-photo product-photo--rack" role="img" aria-label="Photo of a black and red wood piano key coat rack"></div>
    <svg class="card-frame offer-ribbon" width="469" height="300" viewBox="0 0 469 300">
      <circle cx="34" cy="42" r="5" fill="var(--dot-dark)"/>
      <circle cx="48" cy="42" r="5" fill="var(--dot-mid)"/>
      <circle cx="61" cy="42" r="5" fill="var(--offer-red)"/>
      <polyline points="441,60 28,60 28,261" fill="none" stroke="var(--rule)" stroke-width="1.2"/>
      <polygon points="90,61 147,61 28,180 28,123" fill="var(--offer-red)"/>
      <text x="64" y="98" font-size="9" text-anchor="middle" transform="rotate(-45 64 98)">SPECIAL</text>
      <text x="81" y="112" font-size="24" text-anchor="middle" transform="rotate(-45 81 112)">OFFER</text>
    </svg>
    <div class="label label--piano">PIANO KEY</div>
    <div class="label label--size">COAT RACK – LARGE</div>
    <p class="product-copy product-copy--rack">A large wall-mounted coat rack inspired by piano keys. Functional and stylish, offering bold contrast while showcasing smooth wood textures.</p>
    <div class="end-rule end-rule--rack"></div>
  </article>

  <p class="board-note">SQUARE (1:1) → WORKS EVERYWHERE.</p>
</body>
</html>
```